Business Card Design

We need a business card design for a new company based in Melbourne Australia. We are financial broker in finance industry. We provide a wide range of finance solutions to our clients including home loans, commercial loans, business facilities, car loans, equipment loans, invoice finance, etc. The company name is from director's personal name. We would like to have a new company logo that includes TK.

Industry/Entity Type

Business

Contact Information for Business Card

company name: TK & Co Finance Pty Ltd
person's name: Desmond Okafor
role: Managing Director
Mobile: 0417 638 294
fax: 03 9561 4472
Email: desmond.okafor@tkcolending.example
Address: Suite 5/418 Marlow Avenue Elmvale Vic 3174
Credit Licence No.: 718249

```html
<!DOCTYPE html>
<html lang="en">
<head>
<meta charset="utf-8">
<title>TK &amp; Co Finance Pty Ltd — Business Card</title>
<link rel="stylesheet" href="https://fonts.googleapis.com/css2?family=Questrial&display=swap">
<style>
  :root {
    --page: #ececec;
    --card: #ffffff;
    --ink: #1c1c1c;
    --red: #e31e26;
    --black: #1a1a1a;
    --shadow: rgba(0,0,0,0.14);
  }
  * { box-sizing: border-box; margin: 0; padding: 0; }
  html, body { width: 734px; height: 1200px; overflow: hidden; background: var(--page); }
  body { font-family: "Questrial", "Century Gothic", sans-serif; color: var(--ink); position: relative; }

  .card {
    position: absolute; left: 57px; width: 620px; height: 379px;
    background: var(--card); border-radius: 18px; overflow: hidden;
    box-shadow: 0 10px 30px var(--shadow);
  }
  .card--front { top: 150px; }
  .card--back { top: 670px; }

  /* brand lockup */
  .brand { position: absolute; display: flex; align-items: flex-end; gap: 10px; z-index: 1; }
  .brand__mark { font-size: 80px; line-height: 0.8; color: var(--red); letter-spacing: -2px; }
  .brand__name { font-size: 14px; letter-spacing: 2px; color: var(--ink); padding-bottom: 1px; white-space: nowrap; }
  .card--front .brand { left: 50px; top: 238px; }
  .card--back .brand { left: 170px; top: 40px; }

  /* contact block */
  .person { position: absolute; left: 322px; top: 46px; }
  .person__name { font-size: 28px; font-weight: 400; color: var(--ink); }
  .person__role { font-size: 13px; color: var(--red); letter-spacing: 0.5px; margin-top: 2px; }
  .contact { list-style: none; margin-top: 14px; }
  .contact__item { display: flex; align-items: flex-start; gap: 10px; font-size: 14px; line-height: 1.35; margin-bottom: 5px; white-space: nowrap; }
  .contact__icon { width: 14px; height: 14px; flex: none; margin-top: 2px; fill: var(--ink); }

  .licence { position: absolute; left: 50px; bottom: 30px; font-size: 15px; color: var(--red); }
  .licence__number { color: var(--ink); }

  /* back */
  .swoosh { position: absolute; inset: 0; width: 100%; height: 100%; }
  .services { position: absolute; left: 40px; top: 160px; z-index: 1; }
  .services__title { font-size: 17px; font-weight: 400; color: var(--red); margin-bottom: 6px; }
  .services__list { list-style: none; }
  .services__item { display: flex; align-items: center; gap: 9px; font-size: 16px; line-height: 1.6; }
  .tick { width: 15px; height: 15px; flex: none; }
</style>
</head>
<body>

  <section class="card card--front" aria-label="Business card front">
    <div class="person">
      <h1 class="person__name">Desmond Okafor</h1>
      <p class="person__role">MANAGING DIRECTOR</p>
      <ul class="contact">
        <li class="contact__item">
          <svg class="contact__icon" viewBox="0 0 14 14" aria-hidden="true"><path d="M3 0h8a1 1 0 0 1 1 1v12a1 1 0 0 1-1 1H3a1 1 0 0 1-1-1V1a1 1 0 0 1 1-1zm1 2v8h6V2z"/></svg>
          0417 638 294
        </li>
        <li class="contact__item">
          <svg class="contact__icon" viewBox="0 0 14 14" aria-hidden="true"><path d="M3 0h6l2 2v3H3zM1 6h12v6H1zm2 2v1h2V8zm4 0v1h2V8z"/></svg>
          03 9561 4472
        </li>
        <li class="contact__item">
          <svg class="contact__icon" viewBox="0 0 14 14" aria-hidden="true"><path d="M0 2h14v10H0zm1.5 1.2L7 7.5l5.5-4.3z"/></svg>
          desmond.okafor@tkcolending.example
        </li>
        <li class="contact__item">
          <svg class="contact__icon" viewBox="0 0 14 14" aria-hidden="true"><path d="M7 0a5 5 0 0 1 5 5c0 3.5-5 9-5 9S2 8.5 2 5a5 5 0 0 1 5-5zm0 3a2 2 0 1 0 0 4 2 2 0 0 0 0-4z"/></svg>
          <span>Suite 5/418 Marlow Avenue Elmvale<br>Vic 3174</span>
        </li>
      </ul>
    </div>

    <div class="brand">
      <span class="brand__mark">TK</span>
      <span class="brand__name">CO FINANCE PTY LTD</span>
    </div>

    <p class="licence">Credit Licence No.: <span class="licence__number">718249</span></p>
  </section>

  <section class="card card--back" aria-label="Business card back">
    <svg class="swoosh" viewBox="0 0 620 379" preserveAspectRatio="none" aria-hidden="true">
      <path d="M620 80 C570 95 555 190 500 260 C450 325 370 365 290 379 L620 379 Z" fill="var(--black)"/>
      <path d="M620 96 C575 110 565 200 515 268 C468 330 395 368 335 379 L620 379 Z" fill="#ffffff"/>
      <path d="M620 104 C580 118 572 205 523 272 C478 333 408 369 350 379 L620 379 Z" fill="var(--red)"/>
    </svg>

    <div class="brand">
      <span class="brand__mark">TK</span>
      <span class="brand__name">CO FINANCE PTY LTD</span>
    </div>

    <div class="services">
      <h2 class="services__title">Our Services</h2>
      <ul class="services__list">
        <li class="services__item"><svg class="tick" viewBox="0 0 15 15" aria-hidden="true"><rect x="0.5" y="2.5" width="11" height="11" fill="none" stroke="var(--red)"/><path d="M3 8l3 3 8-10" fill="none" stroke="var(--red)" stroke-width="2"/></svg>Home loans</li>
        <li class="services__item"><svg class="tick" viewBox="0 0 15 15" aria-hidden="true"><rect x="0.5" y="2.5" width="11" height="11" fill="none" stroke="var(--red)"/><path d="M3 8l3 3 8-10" fill="none" stroke="var(--red)" stroke-width="2"/></svg>Commercial loans</li>
        <li class="services__item"><svg class="tick" viewBox="0 0 15 15" aria-hidden="true"><rect x="0.5" y="2.5" width="11" height="11" fill="none" stroke="var(--red)"/><path d="M3 8l3 3 8-10" fill="none" stroke="var(--red)" stroke-width="2"/></svg>Business facilities</li>
        <li class="services__item"><svg class="tick" viewBox="0 0 15 15" aria-hidden="true"><rect x="0.5" y="2.5" width="11" height="11" fill="none" stroke="var(--red)"/><path d="M3 8l3 3 8-10" fill="none" stroke="var(--red)" stroke-width="2"/></svg>Car loans</li>
        <li class="services__item"><svg class="tick" viewBox="0 0 15 15" aria-hidden="true"><rect x="0.5" y="2.5" width="11" height="11" fill="none" stroke="var(--red)"/><path d="M3 8l3 3 8-10" fill="none" stroke="var(--red)" stroke-width="2"/></svg>Equipment loans</li>
        <li class="services__item"><svg class="tick" viewBox="0 0 15 15" aria-hidden="true"><rect x="0.5" y="2.5" width="11" height="11" fill="none" stroke="var(--red)"/><path d="M3 8l3 3 8-10" fill="none" stroke="var(--red)" stroke-width="2"/></svg>Invoice finance</li>
      </ul>
    </div>
  </section>

</body>
</html>
```